We need a business card for our gym. We are a LiftCore affiliate in Decatur Georgie established 2008. Our company name is Tarn Functional Fitness. LiftCore Shaping Peak Fitness. Instagram and website is @tarnhall. Hashtags we use #lifewithgrit #madetolift We want something similar to the the black and neon green design attached but a different color scheme. No neon colors. Are company colors are the same as the blue and white card attached. We are open to ideas as far as colors however - just no neon.

Contact Information for Business Card

Tarn Functional Fitness
427 Pellow Drive
Decatur GA 30817
Phone 404.555.0186 Website www.tarnhall.example

Font styles to use
Other font styles liked:
• Futura Extra Bold Condensed

Colors

Designer to choose colors to be used in the design.

Requirements
Must have
• Our primary font we typically use for our name is Futura Extra Bold Condensed
Nice to have
• I attached a card from that is black and neon green from Vexa that we would like something similar. The blue and white is more similar to our colors. We also use have used black and white in the past. We use the chevrons as out logo. We are a LiftCore affiliate so I included a logo from them as well that may or may not be used on the card. Our instagram is @tarnhall hashtags #madetolift #lifewithgrit
Should not have
• No neon colors

```html
<!DOCTYPE html>
<html lang="en">
<head>
<meta charset="utf-8">
<title>Tarn Functional Fitness – Business Card</title>
<link rel="stylesheet" href="https://fonts.googleapis.com/css2?family=Anton&family=Jost:wght@500;600;700&display=swap">
<style>
  :root {
    --navy: #263f5e;
    --navy-deep: #233a58;
    --paper: #eeeff1;
    --white: #ffffff;
    --backdrop: #cbcfd2;
  }
  * { margin: 0; padding: 0; box-sizing: border-box; }
  html, body { width: 1200px; height: 1200px; overflow: hidden; }
  body { background: var(--backdrop); position: relative; font-family: "Jost", sans-serif; color: var(--white); }

  .card { position: absolute; left: 250px; width: 700px; height: 400px; overflow: hidden; }
  .card-front { top: 147px; background: var(--paper); }
  .card-back { top: 652px; background: var(--white); }

  /* Front */
  .chevrons { position: absolute; inset: 0; width: 700px; height: 400px; }
  .chevron-shape { fill: var(--navy); }
  .brand-block { position: absolute; left: 22px; width: 340px; text-align: center; line-height: 1; }
  .brand-name { top: 96px; font-family: "Anton", sans-serif; font-size: 96px; letter-spacing: 4px; }
  .brand-descriptor { top: 195px; font-family: "Anton", sans-serif; font-size: 34px; letter-spacing: 0.5px; }
  .brand-location { top: 257px; font-weight: 600; font-size: 17px; letter-spacing: 6px; }

  /* Back */
  .back-panel { position: absolute; left: 11px; top: 16px; width: 672px; height: 377px; background: var(--navy-deep); }
  .contact-name { position: absolute; left: 33px; top: 23px; font-weight: 700; font-size: 23px; line-height: 1; }
  .contact-row { position: absolute; left: 33px; display: flex; align-items: flex-start; gap: 9px; font-weight: 700; font-size: 21px; line-height: 28px; }
  .contact-row svg { flex: none; width: 22px; height: 22px; margin-top: 3px; }
  .row-address { top: 60px; }
  .row-phone { top: 122px; }
  .row-web { top: 155px; }
  .row-social { top: 189px; }
  .social-dot { flex: none; width: 22px; height: 22px; margin-top: 3px; border-radius: 50%; background: var(--white); }

  .affiliate { position: absolute; left: 458px; top: 50px; display: flex; align-items: center; gap: 10px; font-weight: 700; font-size: 30px; line-height: 1; }
  .affiliate-square { width: 18px; height: 18px; background: var(--white); }

  .hashtag { position: absolute; top: 339px; font-weight: 700; font-size: 16px; line-height: 1; }
  .hashtag-left { left: 55px; }
  .hashtag-right { left: 496px; }
</style>
</head>
<body>

<section class="card card-front" aria-label="Card front">
  <svg class="chevrons" viewBox="0 0 700 400" aria-hidden="true">
    <polygon class="chevron-shape" points="0,0 281,0 466,197 274,400 0,400"/>
    <polygon class="chevron-shape" points="472,0 533,0 700,177 700,220 525,400 460,400 656,192"/>
  </svg>
  <h1 class="brand-block brand-name">TARN</h1>
  <p class="brand-block brand-descriptor">FUNCTIONAL FITNESS</p>
  <p class="brand-block brand-location">DECATUR • GEORGIA</p>
</section>

<section class="card card-back" aria-label="Card back">
  <div class="back-panel">
    <p class="contact-name">Tarn Functional Fitness</p>

    <div class="contact-row row-address">
      <svg viewBox="0 0 24 24" fill="none" stroke="#fff" stroke-width="2"><path d="M12 22s-7-7.5-7-13a7 7 0 0 1 14 0c0 5.5-7 13-7 13z"/><circle cx="12" cy="9" r="2.6"/></svg>
      <span>427 Pellow Drive<br>Decatur GA 30817</span>
    </div>

    <div class="contact-row row-phone">
      <svg viewBox="0 0 24 24" fill="none" stroke="#fff" stroke-width="1.8"><circle cx="12" cy="12" r="10.5"/><path d="M8 6.5l2 2.6-1.2 1.6c.8 1.7 2 2.9 3.6 3.7l1.6-1.2 2.6 2-1.1 2c-4.3-.5-8.2-4.4-8.6-8.7z" fill="#fff"/></svg>
      <span>404.555.0186</span>
    </div>

    <div class="contact-row row-web">
      <svg viewBox="0 0 24 24" fill="none" stroke="#fff" stroke-width="1.5"><circle cx="12" cy="12" r="10"/><ellipse cx="12" cy="12" rx="4.5" ry="10"/><path d="M2 12h20M4 7h16M4 17h16"/></svg>
      <span>www.tarnhall.example</span>
    </div>

    <div class="contact-row row-social">
      <span class="social-dot"></span>
      <span>@tarnhall</span>
    </div>

    <div class="affiliate">
      <span class="affiliate-square"></span>
      <span>LiftCore</span>
    </div>

    <p class="hashtag hashtag-left">#lifewithgrit</p>
    <p class="hashtag hashtag-right">#madetolift</p>
  </div>
</section>

</body>
</html>
```